Apricot Variety Sheet - Cedarline Orchard Growers

We are needing a variety sheet that we can hand out that will describe the different apricot vatieties we have available. The attached document has the name of the variety along with a description that will need to be on the sheet. We are looking for a modern, appealing way to display this information on 1 page (if needed, it can be front and back)
Updates

Apologies for the delay; we are overwhelmed with the great design options and will be sorting through them all (across our contests) to pick a collective. Thank you for your patience.

Target Market(s)

Growers and consumers

Industry/Entity Type

Agriculture

Requirements
Must have
• Easy to read
• Natural color palettes to emphasize the agricultural nature
• Clearly show washington as the origin in the title or at the top
Nice to have
• incorporate Apricots in the design

```html
<!DOCTYPE html>
<html lang="en">
<head>
<meta charset="utf-8">
<title>Washington Apricot Variety Sheet – Cedarline Orchard Growers</title>
<link href="https://fonts.googleapis.com/css2?family=Arimo:wght@400;700&family=Lato:wght@400;900&family=Roboto+Condensed:wght@700&display=swap" rel="stylesheet">
<style>
  :root {
    --backdrop: #6b6b6b;
    --paper: #ffffff;
    --brand-green: #1f6b45;
    --row-dark: rgba(214, 214, 214, 0.95);
    --row-light: rgba(244, 244, 244, 0.95);
    --ink: #222222;
    --wood-light: #efebe6;
  }
  html, body {
    margin: 0;
    padding: 0;
    width: 1200px;
    height: 1200px;
    overflow: hidden;
    background: var(--backdrop);
  }
  .sheet {
    position: absolute;
    left: 212px;
    top: 67px;
    width: 975px;
    height: 1366px;
    background: var(--paper);
    transform: scale(0.8);
    transform-origin: top left;
    overflow: hidden;
  }
  .sheet__photo {
    position: absolute;
    left: 0;
    right: 0;
    bottom: 0;
    height: 560px;
    background:
      radial-gradient(ellipse 260px 150px at 720px 430px, rgba(235, 200, 150, 0.45), transparent 70%),
      radial-gradient(ellipse 300px 160px at 120px 470px, rgba(225, 210, 190, 0.45), transparent 70%),
      linear-gradient(180deg, var(--paper) 0%, var(--wood-light) 45%, #ddd5cc 100%);
  }
  .brand {
    position: absolute;
    top: 26px;
    left: 0;
    right: 0;
    display: flex;
    justify-content: center;
    align-items: center;
    gap: 22px;
  }
  .brand__mark {
    width: 130px;
    height: 130px;
    border-radius: 50%;
    background: var(--brand-green);
  }
  .brand__name {
    font-family: "Lato", sans-serif;
    font-weight: 900;
    font-size: 36px;
    line-height: 1.05;
    color: var(--brand-green);
  }
  .title {
    position: absolute;
    top: 170px;
    left: 0;
    right: 0;
    margin: 0;
    text-align: center;
    font-family: "Roboto Condensed", sans-serif;
    font-weight: 700;
    font-size: 64px;
    line-height: 86px;
    color: var(--brand-green);
    letter-spacing: -0.5px;
  }
  .varieties {
    position: absolute;
    top: 276px;
    left: 57px;
    width: 866px;
    margin: 0;
    padding: 0;
    list-style: none;
  }
  .variety {
    display: flex;
    height: 75px;
    margin-bottom: 4.6px;
  }
  .variety__name {
    width: 247px;
    flex: none;
    background: var(--brand-green);
    color: #fff;
    font-family: "Arimo", sans-serif;
    font-size: 35px;
    display: flex;
    align-items: center;
    justify-content: center;
    border-radius: 2px 0 0 2px;
  }
  .variety__desc {
    flex: 1;
    margin: 0;
    padding: 0 7px 0 9px;
    display: flex;
    align-items: center;
    font-family: "Lato", sans-serif;
    font-size: 15.5px;
    line-height: 19px;
    color: var(--ink);
    border-radius: 0 2px 2px 0;
  }
  .variety:nth-child(odd) .variety__desc { background: var(--row-dark); }
  .variety:nth-child(even) .variety__desc { background: var(--row-light); }
  .website {
    position: absolute;
    top: 1266px;
    left: 0;
    right: 0;
    text-align: center;
    font-family: "Arimo", sans-serif;
    font-weight: 700;
    font-size: 22px;
    letter-spacing: 13px;
    color: var(--ink);
  }
</style>
</head>
<body>
  <main class="sheet">
    <div class="sheet__photo" role="img" aria-label="Faded photo of ripe apricots on a rustic wooden table"></div>

    <header class="brand">
      <div class="brand__mark"></div>
      <div class="brand__name">Cedarline Orchard Growers<br>Washington State</div>
    </header>

    <h1 class="title">Apricot Variety Sheet</h1>

    <ul class="varieties">
      <li class="variety"><span class="variety__name">Rival</span><p class="variety__desc">Great flavor with a fine, firm texture distinguishes this large oval-shaped apricot. The skin is light orange with a red blush. The flesh is a lush deep orange color. Available early July- early August.</p></li>
      <li class="variety"><span class="variety__name">Robada</span><p class="variety__desc">This jumbo apricot has a delicious floral flavor with a firm texture. Bright orange, with a deep red blush over nearly half its surface. Available early June.</p></li>
      <li class="variety"><span class="variety__name">Perfection</span><p class="variety__desc">This classic large oval apricot is deep orange with an oblong shape and firm texture. The flesh is a yellow/orange color that is very sweet and full of flavor. Available mid July - mid August.</p></li>
      <li class="variety"><span class="variety__name">Patterson</span><p class="variety__desc">This apricot has a well-balanced flavor and an excellent shelf life. This is perfect for canning or drying. It has streaked red over yellow skin, with a firm flesh. Available mid – late June.</p></li>
      <li class="variety"><span class="variety__name">Tomcot</span><p class="variety__desc">Tangy, sweet flavor with a firm texture. This oval apricot is light orange with a slight blush color. The flesh is a dark orange. Available late June – late July.</p></li>
      <li class="variety"><span class="variety__name">Casselbrite</span><p class="variety__desc">This medium sized apricot is golden orange with a slight red blush. It has a mild sweet-tart flavor that is good for eating out of hand. Available late June- early July.</p></li>
      <li class="variety"><span class="variety__name">Goldbar</span><p class="variety__desc">Moderately juicy, this large oval-shaped apricot has a light yellow-orange with a reddish blush. The flesh is firm, meaty, and has a light orange color. Available late June – end of July.</p></li>
      <li class="variety"><span class="variety__name">Sweet Juillet</span><p class="variety__desc">This special variety has a unique, sweet flavor with a juicy flesh. It is bright orange in color with a bright orange flesh. Available through July.</p></li>
      <li class="variety"><span class="variety__name">Tasty Rich</span><p class="variety__desc">This early variety is light yellow-orange colored with a firm texture. Very juicy with an enticing flavor. Available through June</p></li>
      <li class="variety"><span class="variety__name">Goldstrike</span><p class="variety__desc">A larger apricot with light orange, blushed skin. Firm texture with a slight tart taste until fully ripened, then very sweet. Available mid June - mid July</p></li>
      <li class="variety"><span class="variety__name">Goldstrike</span><p class="variety__desc">Very aromatic and sweet, this apricot is orange with a red blush. It has a yellow-orange colored flesh and a round shape. Available mid-June to end of July.</p></li>
      <li class="variety"><span class="variety__name">Riland</span><p class="variety__desc">This apricot is round with a bright orange skin color and a deep orange flesh. It has a mild, sweet flavor with a firm texture. Available early July – mid August.</p></li>
    </ul>

    <div class="website">www.cedarlineorchard.com</div>
  </main>
</body>
</html>
```